Web Design for High End Baby Products Gear

We have some work from a designer that just didn't meet standards despite weeks of back and forth. We need someone who can come up with creative colors/fonts/etc. to make the site "pop" and give a clean, inviting feel.

We need three pages designed:

1. Home
2. Category Landing Page
3. Product Detail Page

The current site is www.HappyWheelWalks.com

Please DO NOT use current site for inspiration.

The layout should follow pretty close to what we have attached.

We were not even pleased with the logo so for now we are just concentrating on the colors and aesthetic feel of the site. You can use a nice typography type logo. We will probably have the logo done at a later time. Or if you have any ideas please feel free to submit as it may increase chances of winning design. The layout is pretty much done with the product page layout approved by our paid search people.

This is isn't where you need to spend a lot of time with general layout as it is already pretty much complete but you are free to deviate or make suggestions if you think it will help.

Reason: I haven't been able to provide adequate feedback and want to spend appropriate amount of time doing so.

I posted the set of PSD files that the previous designer completed.  We were not happy with the outcome of this.

I said in my brief "Here are a few like companies:

www.pramvault.com
www.buggynest.com
www.tiddlytopkids.com
www.kplums.com
www.wrenandtilly.com
www.doravimo.com"

What I meant was that these were similar companies to our company with respect to product/customer demographic/etc.

Reason: We have found a few that we really like and are working to determine which designs to continue with.

Thank you for your patience.

Reason: Waiting on feedback from a couple of designers so extending deadline

Thank you all.  We received several designs we really liked.  A couple stood out more than others as they seemed to hit the target on the first go around based on our brief and sample sites submitted.

There are several designers we would like to work with in the future as well as we have about 40 domains we will be developing.

Thank you.

Target Market(s)

Target Market: Female, typically 25-40 yrs old, probably married, probably career minded OR middle to upper middle income (some of our strollers are $500-$1,200), expecting mom or mom, some might have two stroller aged (double strollers). Some of our products are QUALITY (ZEK for jogging or running) or QUALITY with STYLE (Quillaro), but the truth is that this is a WANT not a need. Sure people need A stroller but not a $900 Tessel Stroller. So they have a combination of want and need coupled with ability to pay.

Brand Personality:
Definitely clean, crisp and modern. We want it to “POP” but in color and style. But I guess more directly is we want to be seen as THE or ONE of THE authorities on upper end strollers. Where you can get individual assistance, stroller consultations (yes people call in with their needs and ask advice) and personalized service as opposed to a “big box” type place that tries to be everything to everyone and when you call them you get some guy in a cubicle answering the phone that held his baby niece once. So when someone hits our site or walks into our showroom, they need to know they are in the right place.

Industry/Entity Type

Baby

Requirements
Must have
• Must a clean crisp color scheme, easy to ready, focused on products. Must instill authority, credibility, usability and be simple and uncluttered. Fonts and colors must complement each other to achieve the above.

We need three main images as well for the home page as they will be sliding/rotating images.

Backend is built in Magento so design must conform to that platform.

We retain exlusive rights to the design and all files
Nice to have
• Please see attached word file for more info.

Here are some sites we like:

www.tinyharbor.com
http://www.cubnook.com/
http://www.dapwick.com/
http://www.vemakids.com/index.php
http://www.fernwax.com/
http://www.tana-lume.com/
http://www.grelby.com/
http://www.cardsmithpartners.com/

Keep in mind that I may just like only something about the above sites and not everything. It may be color, it may be layout , font color, use of text on home page, but something about them stands out.

Here are a few like companies:

www.pramvault.com
www.buggynest.com
www.tiddlytopkids.com
www.kplums.com
www.wrenandtilly.com
www.doravimo.com
Should not have
• old dated styles, nothing "frilly"

```html
<!DOCTYPE html>
<html lang="en">
<head>
<meta charset="utf-8">
<title>Happy Wheel Walks – Home</title>
<link rel="stylesheet" href="https://fonts.googleapis.com/css2?family=Dosis:wght@400;500;600;700&family=Open+Sans:wght@400;600;700&display=swap">
<style>
:root{
  --blue:#1b9bd7;
  --blue-dark:#0f7fb9;
  --blue-light:#43bdec;
  --ink:#1d4a6b;
  --muted:#6a7f90;
  --line:#dfe6ec;
  --red:#c8121b;
  --green:#9cc21a;
  --teal:#1ea9c9;
  --white:#ffffff;
  --page:#f3f5f7;
}
*{box-sizing:border-box;margin:0;padding:0}
html,body{width:944px;height:1200px;overflow:hidden;background:var(--page);font-family:"Open Sans",Arial,sans-serif;color:var(--ink)}
.site{position:absolute;left:78px;top:0;width:788px;height:1200px;background:var(--white)}
.abs{position:absolute}

/* header */
.logo{left:16px;top:28px;display:flex;align-items:center;gap:10px}
.logo-dot{width:46px;height:46px;border-radius:50%;background:var(--blue-light)}
.logo-name{font-family:"Dosis",sans-serif;font-weight:700;font-size:24px;line-height:24px;color:#1f5a3c;width:140px}
.promises{left:322px;top:30px;font-family:"Dosis",sans-serif;font-size:15px;line-height:16px;color:#6c6c6c;letter-spacing:.3px}
.toplinks{right:16px;top:6px;font-size:9px;color:var(--ink)}
.toplinks span{margin:0 4px;color:#888}
.search{right:18px;top:24px;display:flex;border:1px solid #cfdbe3;height:28px}
.search .field{width:126px;padding:6px 7px;font-size:12px;color:#7fb7d7}
.search .btn{width:45px;background:#eef2f5;border-left:1px solid #cfdbe3;font-size:11px;color:#6b8192;text-align:center;line-height:26px}
.phone{right:16px;top:68px;text-align:right;font-family:"Dosis",sans-serif;font-weight:700;color:#45a9dd;font-size:20px;line-height:18px}
.phone small{display:block;font-size:13px;font-weight:500;color:#9ccbe6}

/* nav */
.nav{left:0;top:115px;width:788px;height:31px;background:linear-gradient(#3fb7e8,#1090cc)}
.nav ul{list-style:none;display:flex;gap:14px;padding:7px 0 0 7px;font-size:11.5px;color:var(--white)}
.nav li.on{background:var(--white);color:var(--blue-dark);padding:1px 6px;margin-top:-1px;height:19px;font-weight:600}
.social{top:123px;font-family:"Dosis",sans-serif;font-weight:700;font-size:14px;color:var(--white)}
.cart{left:624px;top:109px;width:156px;height:43px;background:var(--red);color:var(--white);font-family:"Dosis",sans-serif;font-weight:600;font-size:16px;display:flex;align-items:center;gap:10px;padding-left:18px;box-shadow:0 2px 3px rgba(0,0,0,.25)}

/* sidebar */
.side{left:14px;top:160px;width:144px}
.news-badge{width:144px;height:62px;background:#e6f4fb;border:1px solid #c7e5f4;text-align:center;font-size:9px;line-height:12px;color:var(--ink);padding-top:9px}
.news-badge b{font-size:12px;font-weight:400;color:var(--blue-dark)}
.side h3{font-family:"Dosis",sans-serif;font-size:17px;font-weight:600;color:#4c5d6a;line-height:16px}
.side h3 small{display:block;font-size:9.5px;font-weight:500;color:#667}
.select{margin-top:4px;height:21px;border:1px solid #c9d2d8;font-size:8.5px;color:#555;padding:4px 6px;position:relative}
.select:after{content:"";position:absolute;right:0;top:0;width:20px;height:19px;border-left:1px solid #c9d2d8;background:linear-gradient(transparent 7px,transparent 7px)}
.side ul{list-style:none;font-size:10px;line-height:14.2px}
.side ul li.head{font-weight:700}
.side .rule{border-bottom:2px solid #cfd7dc;padding-bottom:3px}

/* main */
.hero{left:171px;top:160px;width:603px;height:238px;border:1px solid #cfe0ea;display:flex;justify-content:space-around;align-items:center}
.hero .shot{width:170px;height:210px;border-radius:6px}
.tiles{left:171px;top:411px;display:flex;gap:13px}
.tile{width:192px;height:100px;position:relative;overflow:hidden}
.tile .art{position:absolute;left:0;bottom:0;width:100px;height:72px;border-radius:4px}
.tile h4{position:absolute;right:8px;top:6px;text-align:right;font-family:"Dosis",sans-serif;font-weight:700;font-size:21px;line-height:19px;color:var(--white)}
.tile .cta{position:absolute;right:10px;bottom:10px;background:var(--red);color:var(--white);font-size:10px;font-weight:700;padding:5px 10px;border:1px solid #fff}
.blurb{left:171px;top:524px;width:603px;font-size:9.6px;line-height:12.6px;color:var(--ink)}
.newsbar{left:171px;top:595px;width:396px;height:39px;background:linear-gradient(#b6d733,#93b813);display:flex;align-items:center}
.newsbar .tag{margin-left:14px;width:66px;height:52px;background:var(--red);color:var(--white);font-family:"Dosis",sans-serif;font-weight:700;font-size:19px;display:flex;align-items:center;justify-content:center}
.newsbar p{font-size:11px;line-height:12px;color:var(--white);width:230px;padding-left:10px}
.newsbar .blog{font-family:"Dosis",sans-serif;font-weight:700;font-size:19px;color:var(--white)}
.signup{left:583px;top:595px;width:191px;height:39px;background:linear-gradient(#b6d733,#93b813);display:flex;align-items:center;gap:4px;padding-left:10px}
.signup .field{width:140px;height:20px;background:var(--white);font-size:8.5px;padding:5px 4px}
.signup .go{width:25px;height:20px;background:var(--white);font-size:9.5px;font-weight:700;text-align:center;line-height:20px}
.panel{left:171px;width:603px;border:1px solid var(--line);box-shadow:0 1px 2px rgba(0,0,0,.08)}
.panel h2{height:31px;background:linear-gradient(#23a6df,#0f86c4);color:var(--white);font-family:"Dosis",sans-serif;font-weight:500;font-size:19px;line-height:31px;padding-left:10px}
.panel h2 b{font-weight:700}
.products{display:flex;padding:16px 0 0}
.product{flex:1;text-align:center;border-right:1px solid #eef1f3;font-size:10px;color:#666}
.product:last-child{border:0}
.product .shot{width:86px;height:86px;margin:0 auto 12px;border-radius:6px}
.stars{color:var(--red);font-size:11px;letter-spacing:1px;margin:3px 0}
.stars i{color:#bbb;font-style:normal}
.product small{font-size:8.5px}
.brands{display:flex;justify-content:space-around;align-items:center;height:104px;font-family:"Open Sans",sans-serif;font-size:19px;font-weight:600;color:#2a3640}

/* footer */
.footer{left:0;top:1045px;width:788px;height:155px;background:linear-gradient(#3bb8ea,#2eaee4);color:var(--white)}
.footer .flogo{position:absolute;left:16px;top:43px;display:flex;align-items:center;gap:8px}
.footer .flogo .logo-dot{background:var(--white)}
.footer .flogo .logo-name{color:var(--white);font-size:19px;line-height:19px;width:110px}
.fcol{position:absolute;top:27px;font-size:8.5px;line-height:14px;padding-right:14px;border-right:1px solid rgba(255,255,255,.35);height:110px}
.fcol h5{font-size:9px;font-weight:700;margin-bottom:2px}
.fcol.last{border:0}
.fsocial{position:absolute;left:640px;top:122px;font-family:"Dosis",sans-serif;font-weight:700;font-size:14px}
</style>
</head>
<body>
<div class="site">
  <header>
    <div class="abs logo"><div class="logo-dot"></div><div class="logo-name">HAPPY WHEEL WALKS</div></div>
    <div class="abs promises">365 DAY RETURNS<br>FREE SHIPPING*<br>NO SALES TAX<br>PRICE MATCH GUARANTEE</div>
    <div class="abs toplinks">Registry<span>|</span>Check Out<span>|</span>My Account</div>
    <div class="abs search"><div class="field">Find It!</div><div class="btn">Search</div></div>
    <div class="abs phone">1.877.WHEEL.5<small>(866-555-0142)</small></div>
  </header>

  <nav class="abs nav">
    <ul><li class="on">Home</li><li>Sale</li><li>Gift Registry</li><li>Gift Cards</li><li>Contact Us</li><li>Store Location</li><li>Blog</li></ul>
  </nav>
  <div class="abs social" style="left:468px">Facelink</div>
  <div class="abs social" style="left:545px">Chirper</div>
  <div class="abs cart">
    <svg width="24" height="20" viewBox="0 0 24 20"><path d="M1 2h4l3 11h12l2-8H7" fill="none" stroke="#fff" stroke-width="2.2"/><circle cx="10" cy="17" r="2" fill="#fff"/><circle cx="18" cy="17" r="2" fill="#fff"/></svg>
    View Cart (2)
  </div>

  <aside class="abs side">
    <div class="news-badge"><b>Save 5%</b> when you sign<br>up for our Newsletter,<br>c'mon, dooooo it!</div>
    <h3 style="margin-top:10px"><small>Shop by</small>Brand</h3>
    <div class="select">Select a Brand</div>
    <h3 style="margin-top:22px"><small>Shop by</small>Category</h3>
    <ul style="margin-top:10px">
      <li class="head">Categories ▾</li><li>Baby Strollers (15)</li><li>Child Bike Trailers (10)</li><li>Accessories (30)</li><li>Conversion Kits (16)</li><li>Rain / Sun Covers (7)</li>
    </ul>
    <h3 class="rule" style="margin-top:22px;font-size:14.5px">Refine Results</h3>
    <ul style="margin-top:13px">
      <li class="head">Brand ▾</li><li>Trailo (4)</li><li>ZEK (26)</li><li>Marlow (7)</li><li>Pinecart Carriers (36)</li><li>Brisko (2)</li><li style="text-decoration:underline">See All Brands</li>
    </ul>
    <ul style="margin-top:20px">
      <li class="head">Best use ▾</li><li>Casual (7)</li><li>Cross-training (2)</li><li>Cycling (47)</li><li>Multisport (16)</li><li>Running (5)</li>
    </ul>
  </aside>

  <section class="abs hero">
    <div class="shot" role="img" aria-label="Black jogging stroller" style="background:linear-gradient(#d9dcdf,#6d7277)"></div>
    <div class="shot" role="img" aria-label="Baby resting in a black rocking bouncer" style="background:linear-gradient(#e6e6e6,#55595d)"></div>
    <div class="shot" role="img" aria-label="Stroller with yellow canopy" style="background:linear-gradient(#f2c51f,#4a4e52)"></div>
  </section>

  <section class="abs tiles">
    <div class="tile" style="background:linear-gradient(#32b7e6,#1191cc)"><div class="art" role="img" aria-label="Baby food blender and spoons" style="background:linear-gradient(#b9dc7a,#e27a3c)"></div><h4>STARTING<br>SOLIDS</h4><span class="cta">Check It Out</span></div>
    <div class="tile" style="background:linear-gradient(#a6d04d,#68a526)"><div class="art" role="img" aria-label="Woven wicker basket" style="background:linear-gradient(#c88a4e,#7a4520)"></div><h4>BABY<br>REGISTRY</h4><span class="cta">Know More</span></div>
    <div class="tile" style="background:linear-gradient(#2fc0b8,#12968f)"><div class="art" role="img" aria-label="Plush toy" style="background:linear-gradient(#b07a4c,#6c4427)"></div><h4>NEW<br>ARRIVALS</h4><span class="cta">Take a Look</span></div>
  </section>

  <p class="abs blurb">Lorem ipsum dolor sit amet, consectetur adipiscing elit. Etiam sagittis lorem at libero vestibulum nec rutrum metus consequat. Mauris porttitor orci sit amet sodales ultrices, turpis urna laoreet orci, eget blandit lectus dolor vitae lectus. Phasellus pulvinar rutrum accumsan. Phasellus neque velit, pulvinar eget convallis quis, molestie sed dolor. Phasellus a justo nunc, eget porta ipsum. Phasellus mattis, arcu dignissim faucibus lacinia, massa arcu sagittis enim, vulputate cursus mauris turpis ac sem.</p>

  <div class="abs newsbar"><div class="tag">News</div><p>Our favorite ZOO animals never looked so good (or yummy!)</p><span class="blog">› BLOG</span></div>
  <div class="abs signup"><div class="field">Sign Up for Our Newsletter</div><div class="go">GO</div></div>

  <section class="abs panel" style="top:664px;height:203px">
    <h2>FEATURED <b>PRODUCTS</b></h2>
    <div class="products">
      <div class="product"><div class="shot" role="img" aria-label="Black double stroller" style="background:linear-gradient(#d5d8db,#3d4247)"></div>Price: $250.00<div class="stars">★★★★<i>★</i></div><small>(1 Review)</small></div>
      <div class="product"><div class="shot" role="img" aria-label="Beige bassinet with orange lining" style="background:linear-gradient(#e8833f,#b7a78d)"></div>Price: $250.00<div class="stars">★★★★<i>★</i></div><small>(1 Review)</small></div>
      <div class="product"><div class="shot" role="img" aria-label="Stroller with red canopy" style="background:linear-gradient(#d3283a,#9aa0a5)"></div>Price: $250.00<div class="stars">★★★★<i>★</i></div><small>(1 Review)</small></div>
      <div class="product"><div class="shot" role="img" aria-label="Stroller with multicolour canopy" style="background:linear-gradient(#e34a6a,#3b71c4)"></div>Price: $250.00<div class="stars">★★★★<i>★</i></div><small>(1 Review)</small></div>
      <div class="product"><div class="shot" role="img" aria-label="Beige bassinet with orange lining" style="background:linear-gradient(#e8833f,#b7a78d)"></div>Price: $250.00<div class="stars">★★★★<i>★</i></div><small>(1 Review)</small></div>
    </div>
  </section>

  <section class="abs panel" style="top:885px;height:135px">
    <h2>FEATURED <b>BRANDS</b></h2>
    <div class="brands"><span>Quillaro</span><span>ZEK</span><span>Trailo</span><span>Norvex</span><span>Trailo</span></div>
  </section>

  <footer class="abs footer">
    <div class="flogo"><div class="logo-dot"></div><div class="logo-name">HAPPY WHEEL WALKS</div></div>
    <div class="fcol" style="left:237px"><h5>Company Info.</h5>About Us<br>Jobs at HWW<br>Corporate &amp; Group Sales</div>
    <div class="fcol" style="left:386px"><h5>Products</h5>Gift Registry<br>Gift Cards<br>Sale<br>Shop by Brand<br>Shop by Category<br>Shop by Use</div>
    <div class="fcol" style="left:510px"><h5>Support</h5>Help<br>Contact Us<br>Live Help<br>Order Status<br>Returns &amp; Exchanges<br>Shipping Info.</div>
    <div class="fcol last" style="left:640px"><h5>Legal</h5>Privacy Policy<br>Terms of Use<br>© 2011 by Happy Wheel Walks</div>
    <div class="fsocial">Facelink &nbsp;&nbsp; Chirper</div>
  </footer>
</div>
</body>
</html>
```